Postcard Design

New Integrated low voltage company in Merritt island florida Called Coastline Wiring Associates we offer Integrated Technology for Fire Alarm, Security Systems Access Control Systems CCTV Systems Audio/Video Systems Lighting Control Automation Voice/Data and 24 hour Monitoring Services
Industry/Entity Type
It Company

```html
<!DOCTYPE html>
<html lang="en">
<head>
<meta charset="utf-8">
<title>Coastline Wiring Associates Postcard</title>
<link rel="stylesheet" href="https://fonts.googleapis.com/css2?family=Arimo:wght@400;700&family=Cinzel:wght@600&display=swap">
<style>
  :root {
    --ink: #000000;
    --navy: #0a1a4a;
    --blue: #1f4fb0;
    --sky: #5fa0e6;
    --white: #ffffff;
    --silver: #d9dde3;
    --steel: #8c96a3;
    --tile-cam: #4a4f57;
    --tile-light: #4b5d7e;
    --tile-fire: #b0201c;
    --tile-alarm: #c9c2b4;
  }
  * { margin: 0; padding: 0; box-sizing: border-box; }
  html, body { width: 1200px; height: 936px; overflow: hidden; background: var(--ink); }
  .postcard {
    position: relative; width: 1200px; height: 936px; overflow: hidden;
    background: var(--ink); font-family: "Arimo", Arial, sans-serif; color: var(--white);
  }
  .header-band { position: absolute; left: 0; top: 0; width: 1200px; height: 260px; }
  .company-title {
    position: absolute; right: 48px; top: 28px;
    font-family: "Cinzel", Georgia, serif; font-weight: 600;
    font-size: 44px; letter-spacing: 1px; font-variant: small-caps;
  }
  .brand-mark { position: absolute; left: 58px; top: 86px; width: 250px; height: 250px; }
  .brand-mark .disc {
    position: absolute; inset: 0; border-radius: 50%;
    background: radial-gradient(circle at 40% 35%, var(--blue), var(--navy) 70%);
    border: 6px solid var(--silver);
  }
  .brand-mark .brand-name {
    position: absolute; inset: 0; display: flex; align-items: center; justify-content: center;
    text-align: center; font-weight: 700; font-size: 30px; line-height: 1.15; color: var(--white);
  }
  .headline {
    position: absolute; left: 318px; top: 172px; width: 600px;
    font-weight: 700; font-size: 62px; line-height: 1.12;
  }
  .tagline {
    position: absolute; left: 74px; top: 350px; width: 700px;
    font-weight: 700; font-size: 36px; line-height: 1.3;
  }
  .phone-number {
    position: absolute; left: 74px; top: 508px;
    font-weight: 700; font-size: 50px; letter-spacing: 1px;
  }
  .device-art {
    position: absolute; left: 900px; top: 215px; width: 330px; height: 520px;
    border-radius: 48px; transform: rotate(14deg);
    background: linear-gradient(160deg, #f4f5f7, #bfc4cb 60%, #e7e9ec);
  }
  .service-strip {
    position: absolute; left: 0; top: 728px; width: 1200px; height: 142px;
    background: linear-gradient(180deg, #e9ebee, #b7bcc3);
  }
  .label-bar { position: absolute; left: 0; top: 870px; width: 1200px; height: 66px; background: var(--ink); }
  .service { position: absolute; top: 742px; width: 270px; }
  .service .photo { width: 270px; height: 128px; border: 4px solid var(--white); }
  .service .label {
    margin-top: 22px; text-align: center; font-weight: 700; font-size: 24px;
  }
  .service-cameras { left: 60px; }
  .service-cameras .photo { background: linear-gradient(135deg, #ffffff, var(--tile-cam)); }
  .service-lighting { left: 345px; }
  .service-lighting .photo { background: linear-gradient(180deg, var(--tile-light), #c9883a); }
  .service-fire { left: 615px; }
  .service-fire .photo { background: linear-gradient(135deg, #e2452e, var(--tile-fire)); }
  .service-alarm { left: 885px; }
  .service-alarm .photo { background: linear-gradient(135deg, #f1eee7, var(--tile-alarm)); }
</style>
</head>
<body>
<main class="postcard">
  <svg class="header-band" viewBox="0 0 1200 260" aria-hidden="true">
    <defs>
      <linearGradient id="bandFill" x1="0" y1="0" x2="1" y2="0">
        <stop offset="0" stop-color="#0a1a4a"/>
        <stop offset="0.55" stop-color="#1f4fb0"/>
        <stop offset="1" stop-color="#0d2366"/>
      </linearGradient>
    </defs>
    <path d="M0 0 H1200 V150 C900 230 500 120 0 200 Z" fill="url(#bandFill)"/>
    <path d="M0 200 C500 120 900 230 1200 150" fill="none" stroke="#5fa0e6" stroke-width="4"/>
  </svg>

  <h1 class="company-title">Coastline Wiring Associates</h1>

  <div class="brand-mark">
    <div class="disc"></div>
    <div class="brand-name">Coastline<br>Wiring<br>Associates</div>
  </div>

  <p class="headline">For all of&nbsp; your low voltage needs!</p>
  <p class="tagline">Seamless integration with your smart devices and 24 hour monitoring.</p>
  <p class="phone-number">321-555-0147</p>

  <div class="device-art" role="img" aria-label="Smartphone showing a security event notification"></div>

  <div class="service-strip"></div>
  <div class="label-bar"></div>

  <div class="service service-cameras">
    <div class="photo" role="img" aria-label="Security cameras and recorder"></div>
    <p class="label">Security Cameras</p>
  </div>
  <div class="service service-lighting">
    <div class="photo" role="img" aria-label="Lit outdoor patio at dusk"></div>
    <p class="label">Lighting</p>
  </div>
  <div class="service service-fire">
    <div class="photo" role="img" aria-label="Fire alarm panel and detectors"></div>
    <p class="label">Fire Alarms</p>
  </div>
  <div class="service service-alarm">
    <div class="photo" role="img" aria-label="Alarm system control panel and keypads"></div>
    <p class="label">Alarm Systems</p>
  </div>
</main>
</body>
</html>
```